Corvelle Strategies business card

I need a business card for my new strategic consulting LLC, Corvelle Strategies. We specialize in helping people who care about broadband technology and telecommunications policy, and we're based in Washington DC. I'm looking for a card that says smart, credible, future-facing and signals a high level of expertise. It's DC, so there's clearly a limit to how crazy we can go with this card, but I am looking for a design that reflects a company that is comfortable with technology, policy, and having a little bit fun. I'm uploading my logo below, and I'd like to have it be part of the card design in some fashion.
Target Market(s)
Telecommunications and technology policy professionals
Industry/Entity Type
Technology policy
Contact Information for Business Card
Name of business, my name (Glen Mosswater), email (glen@corvellestrategies-example.com) , phone number (202-555-0148)phone number

```html
<!DOCTYPE html>
<html lang="en">
<head>
<meta charset="utf-8">
<title>Corvelle Strategies – Business Card</title>
<link href="https://fonts.googleapis.com/css2?family=Montserrat:wght@400;500;700;800&display=swap" rel="stylesheet">
<style>
  :root {
    --brand-blue: #0b5cab;
    --brand-blue-dark: #064a8f;
    --brand-blue-light: #1a70bd;
    --accent-gold: #f2ad3a;
    --card-white: #ffffff;
    --card-shade: #eceef1;
    --backdrop: #2a2b2e;
  }
  * { box-sizing: border-box; margin: 0; padding: 0; }
  html, body { width: 1200px; height: 896px; overflow: hidden; }
  body {
    background: var(--backdrop);
    font-family: "Montserrat", sans-serif;
    display: flex;
    align-items: center;
    justify-content: center;
    gap: 40px;
  }
  .card {
    position: relative;
    width: 540px;
    height: 309px;
    border-radius: 18px;
    overflow: hidden;
    box-shadow: 0 18px 40px rgba(0,0,0,.55);
  }
  .card--front {
    background: radial-gradient(ellipse at 35% 70%, var(--brand-blue-light) 0%, var(--brand-blue) 55%, var(--brand-blue-dark) 100%);
    display: flex;
    align-items: center;
    justify-content: center;
  }
  .card--back {
    background: linear-gradient(160deg, var(--card-shade) 0%, var(--card-white) 45%, var(--card-white) 100%);
  }
  .wordmark {
    display: flex;
    align-items: center;
    gap: 12px;
    font-weight: 800;
    letter-spacing: .5px;
    line-height: 1;
  }
  .wordmark__dot {
    width: 26px; height: 26px;
    border-radius: 50%;
    background: var(--accent-gold);
    flex: none;
  }
  .card--front .wordmark { color: var(--card-white); font-size: 38px; }
  .card--back .wordmark {
    position: absolute;
    left: 40px; top: 70px;
    color: var(--brand-blue);
    font-size: 36px;
  }
  .holder {
    position: absolute;
    left: 40px; top: 175px;
    display: flex;
    align-items: flex-start;
    gap: 10px;
  }
  .holder__dash {
    width: 14px; height: 3px;
    background: var(--accent-gold);
    margin-top: 11px;
  }
  .holder__name {
    color: var(--brand-blue);
    font-weight: 700;
    font-size: 22px;
    line-height: 1.05;
    text-transform: uppercase;
  }
  .contact {
    position: absolute;
    right: 26px; top: 172px;
    display: flex;
    align-items: center;
    gap: 10px;
  }
  .contact__icons {
    display: flex;
    flex-direction: column;
    gap: 6px;
    padding: 7px 5px;
    border: 2px solid var(--brand-blue);
    border-radius: 14px;
  }
  .contact__icons svg { width: 14px; height: 14px; display: block; }
  .contact__lines { list-style: none; color: var(--brand-blue); font-size: 11.5px; line-height: 20px; }
  .contact__phone { font-weight: 700; }
  .edge-tab {
    position: absolute;
    left: 200px; bottom: -10px;
    width: 70px; height: 22px;
    border-radius: 10px;
    background: var(--brand-blue);
  }
</style>
</head>
<body>
  <section class="card card--front" aria-label="Card front">
    <div class="wordmark"><span class="wordmark__dot"></span><span>Corvelle Strategies</span></div>
  </section>

  <section class="card card--back" aria-label="Card back">
    <div class="wordmark"><span class="wordmark__dot"></span><span>Corvelle Strategies</span></div>

    <div class="holder">
      <span class="holder__dash"></span>
      <p class="holder__name">Glen<br>Mosswater</p>
    </div>

    <div class="contact">
      <div class="contact__icons">
        <svg viewBox="0 0 16 16" aria-hidden="true"><path fill="#f2ad3a" d="M4 1l3 3-2 2c1 2 3 4 5 5l2-2 3 3-2 3C7 15 1 9 1 3z"/></svg>
        <svg viewBox="0 0 16 16" aria-hidden="true"><rect x="1" y="3" width="14" height="10" rx="1" fill="none" stroke="#f2ad3a" stroke-width="1.6"/><path d="M1 4l7 5 7-5" fill="none" stroke="#f2ad3a" stroke-width="1.6"/></svg>
        <svg viewBox="0 0 16 16" aria-hidden="true"><circle cx="8" cy="8" r="6.5" fill="none" stroke="#f2ad3a" stroke-width="1.6"/><path d="M1.5 8h13M8 1.5c3 3.5 3 9.5 0 13M8 1.5c-3 3.5-3 9.5 0 13" fill="none" stroke="#f2ad3a" stroke-width="1.2"/></svg>
      </div>
      <ul class="contact__lines">
        <li class="contact__phone">(202)-555-0148</li>
        <li>glen@corvellestrategies-example.com</li>
        <li>www.CorvelleStrategies-example.com</li>
      </ul>
    </div>

    <span class="edge-tab"></span>
  </section>
</body>
</html>
```